Business card for STEADYWAVE

Please design professional business card for IT consulting firm STEADYWAVE INC.
Use logo attached.
Use information from sample qNode business card attached.
replace qnode inc with STEADYWAVE INC.
as well as qnodeinc.com with steadywave.example

```html
<!DOCTYPE html>
<html lang="en">
<head>
<meta charset="utf-8">
<title>STEADYWAVE – Business Card</title>
<link href="https://fonts.googleapis.com/css2?family=Poppins:wght@300;600&display=swap" rel="stylesheet">
<style>
  :root {
    --backdrop: #d9d9d9;
    --card: #ffffff;
    --ink: #0d0d0d;
    --ink-soft: #1a1a1a;
    --accent: #8a1fd6;
  }
  * { margin: 0; padding: 0; box-sizing: border-box; }
  html, body {
    width: 1200px;
    height: 1200px;
    overflow: hidden;
    background: var(--backdrop);
    font-family: "Poppins", sans-serif;
    color: var(--ink);
  }
  .card {
    position: absolute;
    left: 194px;
    width: 836px;
    height: 477px;
    background: var(--card);
  }
  .card--front { top: 81px; }
  .card--back { top: 611px; }

  .wordmark {
    display: flex;
    align-items: center;
    font-weight: 600;
    color: var(--ink);
    white-space: nowrap;
  }
  .wordmark__square {
    background: var(--accent);
    display: inline-block;
  }
  .card--front .wordmark {
    position: absolute;
    left: 50%;
    top: 239px;
    transform: translate(-50%, -50%);
    font-size: 66px;
    letter-spacing: 0.06em;
    gap: 22px;
  }
  .card--front .wordmark__square { width: 40px; height: 40px; }

  .card--back .wordmark {
    position: absolute;
    left: 67px;
    top: 58px;
    font-size: 36px;
    letter-spacing: 0.06em;
    gap: 12px;
  }
  .card--back .wordmark__square { width: 22px; height: 22px; }

  .contact {
    position: absolute;
    left: 95px;
    top: 130px;
  }
  .contact__name {
    font-weight: 600;
    font-size: 24px;
    line-height: 1.2;
    letter-spacing: 0.01em;
  }
  .contact__role {
    display: inline-block;
    font-weight: 300;
    font-size: 21px;
    line-height: 1.2;
    margin-top: 3px;
    border-bottom: 1.5px solid var(--ink-soft);
  }
  .contact__list {
    list-style: none;
    margin-top: 20px;
  }
  .contact__list li {
    font-weight: 300;
    font-size: 19.5px;
    line-height: 33.5px;
  }
  .contact__label { font-weight: 600; margin-right: 4px; }
  .company {
    margin-top: 14px;
  }
  .company__name {
    font-weight: 600;
    font-size: 22px;
    line-height: 1.3;
  }
  .company__address {
    font-style: normal;
    font-weight: 300;
    font-size: 19.5px;
    line-height: 31px;
    margin-top: 4px;
  }
</style>
</head>
<body>
  <section class="card card--front">
    <div class="wordmark">STEADYWAVE<span class="wordmark__square"></span></div>
  </section>

  <section class="card card--back">
    <div class="wordmark">STEADYWAVE<span class="wordmark__square"></span></div>
    <div class="contact">
      <h1 class="contact__name">DORIAN VELASKO, P. ENG.</h1>
      <p class="contact__role">GENERAL MANGER</p>
      <ul class="contact__list">
        <li><span class="contact__label">o.</span>(555) 014-2270 ext.201</li>
        <li><span class="contact__label">o.</span>(555) 019-3381</li>
        <li><span class="contact__label">e.</span>dvelasko@steadywave.example</li>
        <li><span class="contact__label">w.</span>www.steadywave.example</li>
      </ul>
      <div class="company">
        <h2 class="company__name">STEADYWAVE INC.</h2>
        <address class="company__address">1820 Harbour Line Rd, Suite 101<br>Lakeview, Ontario, A1B 2C3, Canada</address>
      </div>
    </div>
  </section>
</body>
</html>
```